依頼詳細
サイト構成・基本的な要件については
https://zuvexo.example/boards/R7pQ2mXa9TkWvHcY/B58F3
をご参照ください。

ただ、レイアウトについては、各コンテンツへの導線が確保されていれば、
上記レイアウト案を必ず守る必要はございません。
また、当方jqueryを使用したコーディングも可能です。

提出の写真素材は
https://qlbox.example/T9wRkA
上記のものをご利用いただければ幸いです。

現在、素材があまり集まっていないため、
http://fotmira.example/
などから、10000円程度までならこちらにて購入可能です。
カンプデータにて作成頂き、納品時に当方にて購入したデータに差し替えていただければと存じます。

https://images.velonta.example/jp/
についても定期購入しておりますので、
5点ほどでしたら取得可能です。

また、既存サイト
https://www.harimoku.example/
に使用されている画像は自由にご利用ください。

【参考サイト】
https://www.tzr-worldwide.example/jp/
https://morifusa.example/
https://hotarubako.example/
https://www.calmfield.example/
https://www.yosetabi.example/

写真を大きく見せ、
高級感があり、訴求力の高いデザインを希望します。

色合いは、現在のサイト同様、
モノトーンをベースに、差し色を使用する場合は1色程度、
シックで高級感のある色合いを希望いたします。
サイトURL
ページ数
1ページ
希望イメージ
シンプル 複雑
単色 カラフル
暗い 明るい
日常 高級
遊び心 厳粛
未来的 伝統的
女性的 男性的
希望する色
グレー系
納品ファイル
• 高解像度JPG (.jpg)
• フォトショップ形式 (.psd)
補足説明
提出の写真素材は
https://qlbox.example/T9wRkA
上記アップロードしたものをご利用いただければ幸いです。

現在、素材があまり集まっていないため、
http://fotmira.example/
についても定期購入しておりますので、
5点ほどでしたら取得可能です。

納品データはPSDのほか
XDの提出でも問題ございません。

制作に関してご不明な点がございましたら
お気軽にお申し付けください。

何卒宜しくお願い致します。

```html
<!DOCTYPE html>
<html lang="ja">
<head>
<meta charset="utf-8">
<title>ハリモク | 住空間のリフォーム</title>
<link href="https://fonts.googleapis.com/css2?family=Noto+Serif+JP:wght@400;600&family=Noto+Sans+JP:wght@400;500&display=swap" rel="stylesheet">
<style>
:root{
  --bg:#050505;
  --panel:#1a1a1a;
  --band:#2a2a2a;
  --line:#555;
  --text:#f2f2f2;
  --muted:#bdbdbd;
  --accent:#c8141c;
}
*{margin:0;padding:0;box-sizing:border-box}
html,body{width:1200px;height:2972px;overflow:hidden;background:var(--bg);color:var(--text);font-family:"Noto Sans JP",sans-serif}
.page{position:relative;width:1200px;height:2972px}
.serif{font-family:"Noto Serif JP",serif}

.site-header{position:absolute;top:0;left:0;width:1200px;height:96px;background:#000}
.brand{position:absolute;left:28px;top:22px;display:flex;align-items:center;gap:8px;font-family:"Noto Serif JP",serif;font-weight:600;font-size:22px;letter-spacing:2px;color:var(--text)}
.brand-mark{width:14px;height:14px;border-radius:50%;background:var(--text)}
.global-nav{position:absolute;left:270px;top:66px;display:flex;gap:34px;font-size:13px;color:var(--text)}
.header-contact{position:absolute;right:30px;top:12px;font-size:11px;line-height:18px;color:var(--muted);text-align:left}

.hero{position:absolute;top:96px;left:0;width:1200px;height:832px;background:linear-gradient(100deg,#2b2620 0%,#6b5a48 30%,#cdbfae 55%,#8f7f6e 75%,#3a2e2a 100%)}
.hero-copy{position:absolute;left:0;top:540px;width:1200px;text-align:center}
.hero-copy h1{font-family:"Noto Serif JP",serif;font-weight:600;font-size:26px;letter-spacing:2px;text-shadow:0 1px 6px rgba(0,0,0,.6)}
.hero-copy p{margin-top:14px;font-size:13px;line-height:22px;text-shadow:0 1px 4px rgba(0,0,0,.7)}

.intro{position:absolute;top:990px;left:0;width:1200px}
.intro h2{text-align:center;font-family:"Noto Serif JP",serif;font-weight:600;font-size:19px;letter-spacing:1px}
.intro-body{position:absolute;top:90px;left:160px;width:560px;font-size:13px;line-height:26px;color:var(--muted)}
.intro-body p+p{margin-top:20px}
.intro-photo{position:absolute;top:90px;left:740px;width:440px;height:280px;background:linear-gradient(160deg,#e4e0da,#a89c90 60%,#4a3a32)}

.services{position:absolute;top:1476px;left:0;width:1200px}
.services h2{text-align:center;font-family:"Noto Serif JP",serif;font-size:17px;font-weight:600}
.service-grid{position:absolute;top:62px;left:20px;width:1160px;display:grid;grid-template-columns:repeat(4,1fr);gap:16px 12px}
.service-card{position:relative;height:164px}
.service-card span{position:absolute;left:10px;bottom:10px;font-size:13px;text-shadow:0 1px 4px #000}
.t1{background:linear-gradient(135deg,#3a2e24,#8a6d4c)}.t2{background:linear-gradient(135deg,#d8d2c8,#8e8478)}
.t3{background:linear-gradient(135deg,#2a2a2a,#777068)}.t4{background:linear-gradient(135deg,#e2ddd6,#9a9088)}
.t5{background:linear-gradient(135deg,#4a2a1a,#a86a3a)}.t6{background:linear-gradient(135deg,#6a4a30,#c49a6a)}
.t7{background:linear-gradient(135deg,#1e1e1e,#5a5450)}.t8{background:linear-gradient(135deg,#2a2420,#b8a48a)}

.more-btn{position:absolute;top:1948px;left:510px;width:180px;height:26px;background:#fff;color:#111;font-size:12px;text-align:center;line-height:26px}

.works{position:absolute;top:1996px;left:0;width:1200px}
.works h2{text-align:center;font-family:"Noto Serif JP",serif;font-size:20px;font-weight:600}
.works h2::after{content:"";display:block;width:60px;height:1px;background:var(--text);margin:10px auto 0}
.works-row{position:absolute;top:82px;left:20px;width:1160px;display:grid;grid-template-columns:repeat(5,1fr);gap:8px}
.works-row div{height:200px}
.w1{background:linear-gradient(135deg,#6f8a84,#c8d4cf)}.w2{background:linear-gradient(135deg,#3a3028,#9c8a72)}
.w3{background:linear-gradient(135deg,#5a4434,#c8a47c)}.w4{background:linear-gradient(135deg,#d6d0c8,#7a6e62)}
.w5{background:linear-gradient(135deg,#2e2a26,#a89a88)}

.contact{position:absolute;top:2320px;left:0;width:1200px;height:240px;background:var(--band);text-align:center}
.contact h2{margin-top:48px;font-family:"Noto Serif JP",serif;font-size:22px;font-weight:600}
.contact-line{margin-top:26px;display:flex;justify-content:center;align-items:center;gap:18px}
.contact-line .tel{font-family:"Noto Serif JP",serif;font-size:26px}
.contact-line .hours{font-size:15px}
.contact a{display:inline-block;margin-top:16px;color:var(--text);font-size:14px;text-decoration:underline}

.news{position:absolute;top:2608px;left:0;width:1200px;text-align:center}
.news h2{font-family:"Noto Serif JP",serif;font-size:20px;font-weight:600}
.news ul{list-style:none;margin-top:26px;font-size:12px;line-height:36px;color:var(--muted)}
.news time{margin-right:10px}

.site-footer{position:absolute;top:2820px;left:0;width:1200px;height:152px;border-top:1px solid var(--line)}
.footer-info{position:absolute;left:20px;top:24px;font-size:11px;line-height:34px;color:var(--muted)}
.footer-nav{position:absolute;left:420px;top:24px;width:640px;display:flex;flex-wrap:wrap;gap:10px 28px;font-size:12px}
.copyright{position:absolute;left:0;bottom:14px;width:1200px;text-align:center;font-size:11px;color:var(--muted)}
</style>
</head>
<body>
<div class="page">
  <header class="site-header">
    <div class="brand"><span class="brand-mark"></span>HARIMOKU</div>
    <nav class="global-nav">
      <span>トップページ</span><span>施工事例</span><span>よくある質問</span><span>私たちの強み</span><span>会社概要</span><span>採用情報</span><span>お問い合わせ</span>
    </nav>
    <div class="header-contact">お問い合わせ 0120-418-562<br>受付時間 9:00〜18:00（月〜土）<br>見積り・ご相談は無料です</div>
  </header>

  <section class="hero" role="img" aria-label="明るい木床のキッチンとリビングの室内写真">
    <div class="hero-copy">
      <h1>快適な住空間の演出</h1>
      <p>ひとりひとりの暮らし方に寄り添い、細部までこだわった空間をつくります。<br>デザインと機能性を両立したリフォームで、上質な毎日を。<br>経験豊富なスタッフが、ご相談から完成まで丁寧にお手伝いいたします。</p>
    </div>
  </section>

  <section class="intro">
    <h2>ハリモクは少数精鋭主義にこだわり、一人ひとりにあった住空間をご提案しています</h2>
    <div class="intro-body">
      <p>1998年、株式会社ハリモクは、住宅・店舗・オフィスなどのインテリアデザインを軸に、設計・施工・家具・アートまでを一貫してご提案できる会社として歩みを始めました。</p>
      <p>また、国内外の素材メーカーとの連携により、日本のインテリアデザインにさまざまな新しい価値を生み出してきました。空間全体の調和を大切に、お客様の暮らしにそっと寄り添うデザインを心がけています。</p>
      <p>「住まう方の幸せ」を第一に考え、スタッフ全員が想いを共有しながら、ひとつひとつの現場に真摯に向き合っています。小さなご相談から大規模な改修まで、どうぞお気軽にお声がけください。</p>
      <p>一人ひとりのご要望を丁寧にうかがい、理想の住空間を形にしていきます。私たちと一緒に、心地よい暮らしをつくりませんか。</p>
    </div>
    <div class="intro-photo" role="img" aria-label="ソファとラウンジチェアのあるモダンなリビングの写真"></div>
  </section>

  <section class="services">
    <h2>以下のご質問に対応いたします。お気軽にご相談ください</h2>
    <div class="service-grid">
      <div class="service-card t1" role="img" aria-label="照明の映える店舗内装の写真"><span>デザインリフォーム</span></div>
      <div class="service-card t2" role="img" aria-label="白を基調とした住宅内装の写真"><span>住宅リフォーム</span></div>
      <div class="service-card t3" role="img" aria-label="落ち着いた寝室の写真"><span>寝室リフォーム</span></div>
      <div class="service-card t4" role="img" aria-label="明るいキッチンの写真"><span>キッチン</span></div>
      <div class="service-card t5" role="img" aria-label="木の壁面の店舗内装の写真"><span>店舗デザイン</span></div>
      <div class="service-card t6" role="img" aria-label="ウッドデッキの写真"><span>エクステリア</span></div>
      <div class="service-card t7" role="img" aria-label="浴室の写真"><span>水まわり</span></div>
      <div class="service-card t8" role="img" aria-label="石張りの壁と間接照明の写真"><span>内装仕上げ</span></div>
    </div>
  </section>

  <div class="more-btn">施工事例をすべて見る</div>

  <section class="works">
    <h2>最新施工例</h2>
    <div class="works-row">
      <div class="w1" role="img" aria-label="ガラスブロックの床の施工写真"></div>
      <div class="w2" role="img" aria-label="階段とリビングの施工写真"></div>
      <div class="w3" role="img" aria-label="木のカウンターの施工写真"></div>
      <div class="w4" role="img" aria-label="白いダイニングの施工写真"></div>
      <div class="w5" role="img" aria-label="書棚のある居室の施工写真"></div>
    </div>
  </section>

  <section class="contact">
    <h2>見積無料！まずはお気軽にお問い合わせください</h2>
    <div class="contact-line">
      <svg width="30" height="24" viewBox="0 0 30 24" aria-hidden="true"><path d="M3 8c0-4 24-4 24 0v3h-6V8H9v3H3z" fill="#f2f2f2"/><rect x="6" y="12" width="18" height="10" rx="2" fill="#f2f2f2"/></svg>
      <span class="tel">0120-418-562</span>
      <span class="hours">受付時間　9:00〜18:00(月〜土)</span>
    </div>
    <a>お問い合わせはこちら</a>
  </section>

  <section class="news">
    <h2>新着情報</h2>
    <ul>
      <li><time>2020年11月10日</time>新しい施工事例を公開しました。ぜひご覧ください</li>
      <li><time>2020年11月03日</time>年末年始の営業日についてのお知らせを掲載しました</li>
      <li><time>2020年10月25日</time>ショールーム見学のご予約受付を開始いたしました</li>
    </ul>
  </section>

  <footer class="site-footer">
    <div class="footer-info">TEL.03-5820-4417<br>〒150-0042 東京都渋谷区宇田川町2-11 ハリモクビル3F</div>
    <nav class="footer-nav">
      <span>トップページ</span><span>施工事例</span><span>よくある質問</span><span>私たちの強み</span><span>会社概要</span><span>採用情報</span><span>お問い合わせ</span><span>サイトマップ</span><span>プライバシーポリシー</span>
    </nav>
    <p class="copyright">Copyright © 2020 株式会社ハリモク All Rights Reserved.</p>
  </footer>
</div>
</body>
</html>
```